Business card design for Marion Fitch

I have a logo and will attach. The tag line is: Know your Numbers. The 'K' in Know could be red. There is a registered BAS Agent logo with my number to be incorporated onto the card and my photo (not sure about this though) as mixed reactions to photos on business cards.

I also have a training organisation called, Brightledger College of Tasmania and the red and black 'K" is in this name.

Target Market(s)

Medium to small businesses, tax agents, accountants,

Industry/Entity Type

Financial Service

Contact Information for Business Card

Logo with the name, Tally & Bookkeeping (Registered business name is "PT Tally & Bookkeeping").
My name: Marion Fitch
Email: marion@brcot.com.au
M: 0412 683150
PO Box 7264 Tarrindale Qld 4127.
Web: www.brcot.com.au
Tag line "Know your numbers"

Font styles to use
Serif

Colors
ec1f27
000000

Requirements
Must have
• You can see from the logo 'KK" uploaded that it matches the KK in Bookkeeping, e.g. the second 'K' in Bookkeeping is to be red.
Nice to have
• I have had my photo before, but not so sure this time. Please advise. Landscape design. Clean and clear. White background.

```html
<!DOCTYPE html>
<html lang="en">
<head>
<meta charset="utf-8">
<title>Marion Fitch – Business Card</title>
<link rel="stylesheet" href="https://fonts.googleapis.com/css2?family=Arimo:wght@700&family=Source+Sans+3:wght@400;700&display=swap">
<style>
  :root {
    --brand-red: #ec1f27;
    --ink: #000000;
    --paper: #ffffff;
    --backdrop: #e6e6e6;
    --photo-light: #b9b4b2;
    --photo-dark: #4a3f3d;
  }
  * { margin: 0; padding: 0; box-sizing: border-box; }
  html, body {
    width: 1200px;
    height: 999px;
    overflow: hidden;
    background: var(--backdrop);
  }
  .card {
    position: absolute;
    left: 74px;
    top: 199px;
    width: 1050px;
    height: 600px;
    background: var(--paper);
    overflow: hidden;
  }
  .tagline {
    position: absolute;
    left: 389px;
    top: 88px;
    font-family: "Arimo", Arial, sans-serif;
    font-weight: 700;
    font-size: 57px;
    letter-spacing: -0.5px;
    color: var(--ink);
    line-height: 1;
  }
  .tagline .accent { color: var(--brand-red); }
  .name-band {
    position: absolute;
    left: 0;
    top: 261px;
    width: 100%;
    height: 90px;
    background: var(--brand-red);
  }
  .name {
    position: absolute;
    left: 393px;
    top: 278px;
    font-family: "Arimo", Arial, sans-serif;
    font-weight: 700;
    font-size: 52px;
    color: var(--paper);
    line-height: 1;
  }
  .portrait {
    position: absolute;
    left: 62px;
    top: 123px;
    width: 296px;
    height: 380px;
  }
  .contact {
    position: absolute;
    left: 390px;
    top: 373px;
    font-family: "Source Sans 3", "Myriad Pro", sans-serif;
    color: var(--ink);
  }
  .address {
    font-size: 24px;
    line-height: 32px;
    margin-left: 2px;
  }
  .contact-line {
    display: flex;
    align-items: center;
    gap: 14px;
    font-size: 24px;
    line-height: 32px;
    margin-top: 10px;
  }
  .contact-line svg { width: 26px; height: 26px; flex: none; }
  .phone {
    display: flex;
    align-items: center;
    gap: 14px;
    font-size: 46px;
    font-weight: 700;
    line-height: 50px;
    margin-top: 8px;
  }
  .phone svg { width: 30px; height: 30px; flex: none; }
</style>
</head>
<body>
  <section class="card">
    <h1 class="tagline"><span class="accent">K</span>now your numbers</h1>

    <div class="name-band"></div>
    <h2 class="name">Marion Fitch</h2>

    <svg class="portrait" viewBox="0 0 296 380" role="img" aria-label="Portrait photo of Marion Fitch">
      <defs>
        <linearGradient id="portrait-tone" x1="0" y1="0" x2="0" y2="1">
          <stop offset="0" stop-color="var(--photo-light)"/>
          <stop offset="0.6" stop-color="var(--photo-dark)"/>
          <stop offset="1" stop-color="var(--brand-red)"/>
        </linearGradient>
      </defs>
      <ellipse cx="148" cy="190" rx="143" ry="186" fill="var(--brand-red)"/>
      <ellipse cx="148" cy="190" rx="135" ry="178" fill="url(#portrait-tone)"/>
    </svg>

    <div class="contact">
      <p class="address">PO Box 7264 Tarrindale Qld 4127.</p>
      <p class="contact-line">
        <svg viewBox="0 0 24 24" aria-hidden="true"><path d="M2 10 L12 3 L22 10 V21 H2 Z" fill="var(--ink)"/><path d="M4 11 L12 16 L20 11" fill="none" stroke="var(--paper)" stroke-width="1.8"/></svg>
        <span>marion@brcot.com.au</span>
      </p>
      <p class="contact-line">
        <svg viewBox="0 0 24 24" aria-hidden="true"><path d="M21 3 L17 18 L13 14 L6 21 L3 18 L10 11 L6 7 Z" fill="var(--ink)"/></svg>
        <span>www.brcot.com.au</span>
      </p>
      <p class="phone">
        <svg viewBox="0 0 24 24" aria-hidden="true"><path d="M6.6 2.5 L9.6 6.8 L7.7 9 C8.8 11.6 11.6 14.6 14.8 16.2 L17 14.3 L21.5 17.2 L19.6 21 C11.8 21 3 12.4 3 4.4 Z" fill="var(--ink)"/><path d="M14 3.5 A7 7 0 0 1 20.5 10 M14 7 A3.6 3.6 0 0 1 17 10" fill="none" stroke="var(--ink)" stroke-width="1.8"/></svg>
        <span>0412 683150</span>
      </p>
    </div>
  </section>
</body>
</html>
```